Solace Chiropractic & Acupuncture Business Cards

I need a business card design that feels elevated. I am open to any of the logo designs uploaded. We have two doctors so I'll need to be able to change out the names.

Information:
Marnie Toller D.C., L.Ac., MSOM
584 W 12th St, Ste 320
Larkspur, NE 68419
solacegrove.net
402-555-0147
drmarnie@solacegrove.com
Updates

We have designs we like now, we are just trying to choose between top contenders. Thanks for your submissions!

Contact Information for Business Card

noted in description

Requirements
Must have
• ability to edit info if possible
Nice to have
• Please see our website solacegrove.net for our style and colors

```html
<!DOCTYPE html>
<html lang="en">
<head>
<meta charset="utf-8">
<title>Solace Chiropractic &amp; Acupuncture — Business Card</title>
<link href="https://fonts.googleapis.com/css2?family=Cormorant+Garamond:wght@500;600&family=Lato:wght@400;700&display=swap" rel="stylesheet">
<style>
  :root {
    --navy: #363f54;
    --taupe: #c9beb6;
    --taupe-light: #d3cbc2;
    --sand-text: #d6cdc2;
    --paper: #ffffff;
    --canvas: #ffffff;
  }
  * { box-sizing: border-box; margin: 0; padding: 0; }
  html, body { width: 1200px; height: 1000px; overflow: hidden; background: var(--canvas); }
  .canvas { position: relative; width: 1200px; height: 1000px; }
  .card {
    position: absolute; left: 254px; width: 693px; height: 395px;
    border-radius: 46px; overflow: hidden;
    box-shadow: 0 2px 5px rgba(0,0,0,0.22);
  }
  .card-front { top: 78px; background: var(--paper); }
  .card-back { top: 527px; background: var(--taupe); }
  .front-shape { position: absolute; inset: 0; }
  .brand-mark {
    position: absolute; left: 60px; top: 118px; width: 170px;
    display: flex; flex-direction: column; align-items: center; gap: 16px;
  }
  .brand-dot { width: 112px; height: 112px; border-radius: 50%; background: var(--taupe-light); }
  .brand-name-small {
    font-family: "Cormorant Garamond", serif; font-weight: 600;
    font-size: 34px; line-height: 1; color: var(--navy); letter-spacing: 1px;
  }
  .details { position: absolute; left: 379px; top: 94px; color: #fff; font-family: "Lato", sans-serif; }
  .doctor-name {
    font-family: "Cormorant Garamond", serif; font-weight: 600;
    font-size: 27px; letter-spacing: 1px; color: var(--sand-text);
    line-height: 1; white-space: nowrap;
  }
  .credentials { font-weight: 700; font-size: 16.5px; margin-top: 5px; white-space: nowrap; }
  .contact-list { list-style: none; margin-top: 22px; font-size: 15.5px; white-space: nowrap; }
  .contact-item { position: relative; padding-left: 21px; line-height: 20px; }
  .contact-item + .contact-item { margin-top: 4px; }
  .contact-item.address { margin-bottom: 10px; }
  .contact-item .practice { font-weight: 700; }
  .icon { position: absolute; left: 0; top: 4px; width: 12px; height: 12px; }
  .back-brand {
    position: absolute; inset: 0; display: flex; flex-direction: column;
    align-items: center; justify-content: center; color: var(--navy);
    font-family: "Cormorant Garamond", serif; font-weight: 600;
  }
  .back-name { font-size: 128px; line-height: 0.9; letter-spacing: 1px; }
  .back-tagline { font-size: 19px; letter-spacing: 0.5px; text-transform: uppercase; margin-top: 12px; }
</style>
</head>
<body>
<div class="canvas">
  <section class="card card-front">
    <svg class="front-shape" viewBox="0 0 693 395" width="693" height="395" aria-hidden="true">
      <path fill="var(--taupe-light)" d="M328 36 C346 110 334 160 304 222 C278 282 284 336 328 388 C290 344 268 284 292 216 C318 150 338 104 328 36 Z"/>
      <path fill="var(--navy)" d="M309 0 C360 62 362 122 322 192 C284 262 290 336 344 395 L693 395 L693 0 Z"/>
    </svg>
    <div class="brand-mark">
      <div class="brand-dot"></div>
      <div class="brand-name-small">Solace</div>
    </div>
    <div class="details">
      <h1 class="doctor-name">DR. MARNIE TOLLER</h1>
      <p class="credentials">D.C., L.Ac., MSOM</p>
      <ul class="contact-list">
        <li class="contact-item address">
          <svg class="icon" viewBox="0 0 12 12"><path fill="var(--taupe)" d="M6 0a4 4 0 0 0-4 4c0 3 4 8 4 8s4-5 4-8a4 4 0 0 0-4-4zm0 5.6a1.6 1.6 0 1 1 0-3.2 1.6 1.6 0 0 1 0 3.2z"/></svg>
          <span class="practice">Solace Chiropractic &amp; Acupuncture</span><br>
          584 W 12th St, Ste 320<br>
          Larkspur, NE 68419
        </li>
        <li class="contact-item">
          <svg class="icon" viewBox="0 0 12 12"><path fill="var(--taupe)" d="M2.5 0.5l2 2.2-1 1.3c.8 1.7 2 2.9 3.6 3.6l1.3-1 2.2 2-1.2 1.8C5 10 1.5 6.5.7 1.7z"/></svg>
          402-555-0147
        </li>
        <li class="contact-item">
          <svg class="icon" viewBox="0 0 12 12"><path fill="var(--taupe)" d="M0 2.5h12v7H0z"/><path fill="none" stroke="var(--navy)" stroke-width="1" d="M0.5 3l5.5 3.6L11.5 3"/></svg>
          drmarnie@solacegrove.com
        </li>
        <li class="contact-item">
          <svg class="icon" viewBox="0 0 12 12"><circle cx="6" cy="6" r="5.5" fill="var(--taupe)"/><path fill="none" stroke="var(--navy)" stroke-width="0.9" d="M0.5 6h11M6 0.5c-2.2 2.5-2.2 8.5 0 11M6 0.5c2.2 2.5 2.2 8.5 0 11"/></svg>
          www.solacegrove.net
        </li>
      </ul>
    </div>
  </section>

  <section class="card card-back">
    <div class="back-brand">
      <div class="back-name">Solace</div>
      <div class="back-tagline">Chiropractic &amp; Acupuncture</div>
    </div>
  </section>
</div>
</body>
</html>
```